Vina Lumbral

Lumbral embodies the purity and intensity of Chile’s cold coastal terroir. The sleek white label and bold X logo reflect the stark beauty and unrelenting nature of these extreme winemaking conditions. Crisp, vibrant, and refreshingly bold, Lumbral is a tribute to the wild energy of the Pacific winds and the cool embrace of the coastal valleys—a wine for those who seek purity and perfection in every sip. We would like to have a simple design focusing o the X, we try some option see attach but we are no satisfied is not enaguh eyes catching
Updates

Please create a mysterious, enigmatic label based on the typography and logo attached to the project. We need at least, at the entry level, five varietal products such as Carménère, Cabernet Sauvignon, Merlot, Chardonnay, and Malbec. Later, we would like to add more premium products, like a Reserva, a Special Reserva, or a Limited Edition. The design should be flexible and easily adaptable to accommodate various products while maintaining the same overall aesthetic.

I upload some wines label with printing technic we would like to use on our label, please incorporate this into your design

Project Brief – Large-Scale Brand Label Design
We are developing a new large-scale brand with a structured range of wines. Below are the key design elements and specifications for the labels:

Pinot Noir, Chardonnay, Syrah (Burgundy bottle shape – must include "Special Reserve" on the label)
General Label Guidelines
Year: Only mention "2024" (do not include the word “vintage”).
Capsules: Use standard-colored capsules only (no branding).
Label Design:
Focus on the label itself; bottle and background are irrelevant.
We can consider a wraparound label, but space must be reserved for back-label information.
Please refer to www.corlenti-wines.example for brand coherence. Let us know if further details are needed.

Target Market(s)

peopels who looking for simple design but strinking with the X . THe X could be like a painting brush somehting which make it look artistic

Industry/Entity Type

Wines producer

Font styles to use
Decorative
Script
Other font styles liked:
• the X would be nice if it look like he is Brush from a painter

Colors
0054AA
0677BA
7BADD7
CADEEF
E8F1F8
FFF300
FFF600
FEFA6F
FFFEC7
FFFEE8
EB3D1F
EC4F4E
F09395
F8D3D4
FCEDEE

Requirements
Must have
• We need to indicate the varietals Cabernet Sauvignon, the vintage 2024, the region DO Central Valley
Nice to have
• option on a burgendy bottle for chardonnay and pinot noir and option on bordeau bottle for Cabernet sauvignon and Merlot, We will need a large serie of 5 entrance lebvel (4 red one white) 2 reserve, 2 special reserve, 2 Limited

```html
<!DOCTYPE html>
<html lang="en">
<head>
<meta charset="utf-8">
<title>Lumbral – Varietal Labels</title>
<link rel="stylesheet" href="https://fonts.googleapis.com/css2?family=Cormorant+Garamond:wght@500;600&family=Montserrat:wght@400&display=swap">
<style>
  :root {
    --canvas: #f4f4f4;
    --label-paper: #f7f7f6;
    --ink: #1e1e1e;
    --ink-soft: #3a3a3a;
    --orange-light: #f6b12c;
    --orange: #ec8a16;
    --orange-deep: #d8650d;
    --blue-light: #7badd7;
    --blue: #0677ba;
    --blue-deep: #0054aa;
    --shadow: rgba(0, 0, 0, 0.10);
  }
  * { margin: 0; padding: 0; box-sizing: border-box; }
  html, body {
    width: 1000px;
    height: 1200px;
    overflow: hidden;
    background: var(--canvas);
  }
  .label-range {
    position: relative;
    width: 1000px;
    height: 1200px;
  }
  .label {
    position: absolute;
    background: var(--label-paper);
    box-shadow: 0 2px 14px var(--shadow);
    overflow: hidden;
  }
  .label--cabernet { left: 50px; top: 240px; width: 420px; height: 660px; }
  .label--chardonnay { left: 520px; top: 390px; width: 430px; height: 510px; }

  .brush-art {
    position: absolute;
    left: 50%;
    transform: translateX(-50%);
    border-radius: 6px;
  }
  .label--cabernet .brush-art {
    top: 60px; width: 280px; height: 310px;
    background: radial-gradient(ellipse at 50% 50%, var(--orange) 0%, var(--orange-light) 45%, rgba(246,177,44,0.25) 72%, rgba(247,247,246,0) 100%);
  }
  .label--chardonnay .brush-art {
    top: 30px; left: 46%; width: 270px; height: 290px;
    background: radial-gradient(ellipse at 50% 50%, var(--blue-deep) 0%, var(--blue) 42%, rgba(123,173,215,0.3) 72%, rgba(247,247,246,0) 100%);
  }

  .brand-name {
    position: absolute;
    left: 0; right: 0;
    text-align: center;
    font-family: "Cormorant Garamond", Georgia, serif;
    font-weight: 600;
    color: var(--ink);
    letter-spacing: 1px;
  }
  .label--cabernet .brand-name { top: 390px; font-size: 64px; }
  .label--chardonnay .brand-name { top: 328px; left: -20px; font-size: 56px; }

  .varietal {
    position: absolute;
    left: 0; right: 0;
    text-align: center;
    font-family: "Cormorant Garamond", Georgia, serif;
    font-weight: 500;
    color: var(--ink-soft);
    text-transform: uppercase;
    letter-spacing: 2px;
    line-height: 1.25;
  }
  .label--cabernet .varietal { top: 496px; font-size: 22px; }
  .varietal__year { font-size: 19px; }
  .label--chardonnay .varietal { top: 408px; left: -20px; font-size: 21px; }

  .region {
    font-family: "Montserrat", Arial, sans-serif;
    font-weight: 400;
    color: var(--ink-soft);
    text-transform: uppercase;
    letter-spacing: 5px;
    font-size: 11px;
  }
  .label--cabernet .region {
    position: absolute;
    left: 0; right: 0; top: 572px;
    text-align: center;
  }
  .label--chardonnay .region {
    position: absolute;
    right: 6px; top: 40px;
    writing-mode: vertical-rl;
    transform: rotate(180deg);
    font-size: 8px;
    letter-spacing: 3px;
  }

  .edge-band {
    position: absolute;
    left: 0; right: 0; bottom: 0;
    display: block;
  }
  .label--cabernet .edge-band { height: 40px; }
  .label--chardonnay .edge-band { height: 40px; }
</style>
</head>
<body>
<main class="label-range">

  <section class="label label--cabernet">
    <div class="brush-art" role="img" aria-label="Painted orange brush-stroke artwork"></div>
    <h1 class="brand-name">Lumbral</h1>
    <p class="varietal">Cabernet Sauvignon<br><span class="varietal__year">Vintage 2024</span></p>
    <p class="region">DO Central Valley</p>
    <svg class="edge-band" viewBox="0 0 420 40" preserveAspectRatio="none" role="img" aria-label="Orange painted edge band">
      <defs>
        <linearGradient id="band-orange" x1="0" x2="1" y1="0" y2="0">
          <stop offset="0" stop-color="var(--orange-light)"/>
          <stop offset="1" stop-color="var(--orange-deep)"/>
        </linearGradient>
      </defs>
      <polygon points="0,26 140,22 300,14 420,6 420,40 0,40" fill="url(#band-orange)"/>
    </svg>
  </section>

  <section class="label label--chardonnay">
    <div class="brush-art" role="img" aria-label="Painted blue brush-stroke artwork"></div>
    <p class="region">DO Central Valley</p>
    <h2 class="brand-name">Lumbral</h2>
    <p class="varietal">Chardonnay 2024</p>
    <svg class="edge-band" viewBox="0 0 430 40" preserveAspectRatio="none" role="img" aria-label="Blue painted edge band">
      <defs>
        <linearGradient id="band-blue" x1="0" x2="1" y1="0" y2="0">
          <stop offset="0" stop-color="var(--blue-deep)"/>
          <stop offset="1" stop-color="var(--blue)"/>
        </linearGradient>
      </defs>
      <polygon points="0,28 150,24 310,18 430,8 430,40 0,40" fill="url(#band-blue)"/>
    </svg>
  </section>

</main>
</body>
</html>
```